Website Redesign - We Need Your Magic!

Hello we are looking for you to help us re-design a high end and professional website for a high-end private school.

Here is the current site: http://www.veltrasham.example/

NOTE THIS IS DESIGN ONLY, NO CODING :)

The image they want to portray is that of high quality sports and education, in a creative "un-stiff" way.

Menu Bar: Horizontal

Look and Feel:

Site Colors: Dark green and a Gold yellow (logos are attached)

This site will represent a school so the look must be clean, bold, and classy. The site must have a very clean user interface, with things easily recognizable. Think simple.

The site should be visually appealing! If you come to me with templates, or a ton of text you will be out.

This site should be outside the box, we do not want boring, we do not want status quo. This site should instill excitement, innovation, and athletics.

So the main points again are:

1. High-end and classy look, with creative feel
2. Simple and clear navigation style
3. To cover the Junior and High School - Veltrasham College Schools

Think outside the box. We look forward to seeing what you come up with!!

Thank you for helping us create an amazing site for the school!

Industry/Entity Type

School

```html
<!DOCTYPE html>
<html lang="en">
<head>
<meta charset="utf-8">
<title>Veltrasham College</title>
<link href="https://fonts.googleapis.com/css2?family=Oswald:wght@400;500&family=Open+Sans:wght@400;600&display=swap" rel="stylesheet">
<style>
:root{
  --green:#0c5a20;
  --green-dark:#07481a;
  --green-text:#147a2c;
  --yellow:#f3e316;
  --ink:#222;
  --body:#444;
  --row:#e4e4e4;
  --rule:#dcdcdc;
  --white:#fff;
}
*{box-sizing:border-box;margin:0;padding:0}
html,body{width:1200px;height:2769px;overflow:hidden;background:var(--white)}
body{font-family:"Open Sans",Arial,sans-serif;color:var(--body);position:relative}
.heading{font-family:"Oswald",Arial,sans-serif;font-weight:500;font-size:24px;color:var(--ink);text-transform:uppercase;letter-spacing:.3px;position:relative;padding-bottom:12px}
.heading span{color:var(--green-text)}
.heading::after{content:"";position:absolute;left:0;bottom:0;width:46px;height:4px;background:var(--green)}
.wrap{position:absolute;left:161px;width:877px}

/* header */
.site-header{position:absolute;top:0;left:0;width:1200px;height:138px;background:var(--green)}
.brand{position:absolute;left:166px;top:18px;display:flex;align-items:center;gap:10px}
.brand-dot{width:54px;height:54px;border-radius:50%;background:var(--yellow)}
.brand-name{font-family:"Oswald",sans-serif;font-weight:500;font-size:20px;color:var(--yellow);text-transform:uppercase;line-height:1.1;width:110px}
.info-call{position:absolute;left:653px;top:22px;display:flex;gap:10px;align-items:flex-start}
.info-call small{display:block;font-family:"Oswald",sans-serif;font-size:13px;color:var(--white);letter-spacing:.5px}
.info-call strong{display:block;font-family:"Oswald",sans-serif;font-weight:500;font-size:27px;color:var(--yellow);line-height:1.1}
.search{position:absolute;left:865px;top:22px}
.search small{display:block;font-family:"Oswald",sans-serif;font-size:13px;color:var(--white);letter-spacing:.5px;margin-bottom:4px}
.search-box{width:175px;height:26px;background:var(--white);border-radius:2px;font-size:11px;color:#888;padding:5px 8px;position:relative}
.search-box svg{position:absolute;right:7px;top:6px}
.nav{position:absolute;left:353px;top:93px;display:flex;gap:28px;list-style:none}
.nav li{font-family:"Oswald",sans-serif;font-size:14.5px;color:var(--white);text-transform:uppercase;padding-bottom:8px}
.nav li.active{border-bottom:3px solid var(--yellow)}

/* hero */
.hero{position:absolute;top:138px;left:0;width:1200px;height:480px;display:grid;grid-template-columns:242px 238px 240px 238px 242px;grid-template-rows:240px 240px}
.tile{display:block}

/* welcome */
.welcome{top:662px}
.welcome-text{width:485px;margin-top:22px;font-size:12.5px;line-height:1.65}
.welcome-text p+p{margin-top:16px}
.video{position:absolute;left:524px;top:3px;width:353px;height:235px;background:linear-gradient(160deg,#6f7c5a,#9aa37a 45%,#4c5d34)}
.video svg{position:absolute;left:152px;top:92px}
.rule{position:absolute;left:161px;width:877px;height:1px;background:var(--rule)}

/* notes */
.notes{top:990px;display:flex;gap:0}
.note{width:438px;padding-right:30px}
.note + .note{padding-left:26px;padding-right:0;border-left:1px solid var(--rule)}
.note-body{display:flex;gap:18px;margin-top:30px}
.note-photo{flex:none;width:150px;height:150px}
.note-copy{font-size:12.2px;line-height:1.72}
.btn-outline{display:inline-block;margin-top:14px;border:2px solid var(--green);border-radius:3px;font-size:11px;color:var(--green);padding:2px 10px}

/* calendar */
.calendar{top:1345px}
.cal{margin-top:22px;width:877px;border-collapse:collapse;font-size:12px;color:#333}
.cal th{font-family:"Oswald",sans-serif;font-weight:400;font-size:17px;color:var(--green-text);text-transform:uppercase;height:48px}
.cal td{text-align:center;line-height:1.45}
.cal td.label{text-align:left;padding-left:12px;font-family:"Oswald",sans-serif;font-weight:500;font-size:16px;color:#222;width:270px;text-transform:uppercase}
.cal tr.shade td{background:var(--row)}
.cal tbody tr{height:57px}
.cal tbody tr.shade{height:45px}

/* downloads */
.downloads{top:1765px;height:109px;background:var(--green);display:flex;gap:22px;padding:30px 0 0 150px;border-bottom:4px solid var(--green-dark)}
.btn-yellow{width:276px;height:48px;background:var(--yellow);font-family:"Oswald",sans-serif;font-weight:500;font-size:15px;color:#1c1c1c;text-transform:uppercase;display:flex;align-items:center;justify-content:center;border-radius:2px}

/* events */
.events{top:1915px;width:620px}
.event-list{display:flex;gap:22px;margin-top:22px}
.event{width:202px}
.event-photo{height:132px}
.event-date{font-family:"Oswald",sans-serif;font-size:15.5px;color:#222;margin-top:18px;text-transform:uppercase}
.event-title{font-size:11.5px;color:#444;margin-top:4px}
.sports{position:absolute;left:674px;top:0;width:203px}
.sports ul{list-style:none;margin-top:22px;font-size:12px;line-height:2.1;color:#333}

/* partners */
.partners{top:2253px;display:flex;gap:74px;padding-left:27px}
.partner{width:150px;height:92px;border:1px solid #d6d6d6;display:flex;align-items:center;justify-content:center}
.partner i{display:block;width:100px;height:44px;background:#e8e8e8;border-radius:4px}

/* footer */
.site-footer{position:absolute;left:0;top:2400px;width:1200px;height:323px;background:var(--green)}
.footer-title{color:var(--white)}
.footer-title span{color:var(--yellow)}
.footer-title::after{background:var(--yellow)}
.contacts{position:absolute;left:161px;top:40px;width:580px}
.contact-grid{display:grid;grid-template-columns:340px 230px;row-gap:50px;margin-top:38px}
.contact{display:flex;gap:16px;font-size:11.5px;color:var(--white);line-height:1.55}
.contact strong{display:block;font-family:"Oswald",sans-serif;font-weight:500;font-size:13px;color:var(--yellow);text-transform:uppercase}
.contact svg{flex:none}
.newsletter{position:absolute;left:760px;top:-30px;width:278px;height:353px;background:var(--green-dark);padding:28px 26px}
.newsletter::before{content:"";position:absolute;left:0;top:0;width:12px;height:30px;background:var(--green-dark);transform:translateX(-12px) skewY(0)}
.newsletter p{font-size:11.5px;color:var(--white);line-height:1.65;margin-top:26px}
.field{height:30px;background:var(--white);border-radius:2px;font-size:11px;color:#777;padding:7px 10px;margin-top:10px}
.field:first-of-type{margin-top:16px}
.news-btns{display:flex;gap:10px;margin-top:16px}
.news-btns span{font-family:"Oswald",sans-serif;font-weight:500;font-size:14px;padding:6px 14px;text-transform:uppercase}
.subscribe{background:var(--yellow);color:#1a1a1a}
.unsubscribe{background:#093c15;color:var(--white)}
.bottom-bar{position:absolute;left:161px;top:2735px;width:877px;display:flex;justify-content:space-between;align-items:center;font-size:11px;color:#444}
.social{display:flex;gap:6px;align-items:center}
.social i{display:block;width:16px;height:16px;border-radius:50%}
.social b{display:block;width:34px;height:16px;background:#e4e4e4;border-radius:2px;margin-right:4px}
</style>
</head>
<body>

<header class="site-header">
  <div class="brand"><span class="brand-dot"></span><span class="brand-name">Veltrasham College</span></div>
  <div class="info-call">
    <svg width="18" height="28" viewBox="0 0 18 28"><rect x="1" y="1" width="16" height="26" rx="2" fill="none" stroke="#fff" stroke-width="2"/><rect x="4" y="4" width="10" height="14" fill="#fff"/><circle cx="9" cy="22.5" r="1.6" fill="#fff"/></svg>
    <div><small>INFORMATION CALL</small><strong>0772 918 304</strong></div>
  </div>
  <div class="search">
    <small>SEARCH NOW!</small>
    <div class="search-box">Enter Your Keyword...
      <svg width="12" height="12" viewBox="0 0 12 12"><circle cx="5" cy="5" r="3.6" fill="none" stroke="#777" stroke-width="1.5"/><path d="M8 8l3 3" stroke="#777" stroke-width="1.5"/></svg>
    </div>
  </div>
  <ul class="nav">
    <li class="active">Home</li><li>About</li><li>Academics</li><li>Sports</li><li>Joining Veltrasham</li><li>Working at the College</li><li>Contact</li>
  </ul>
</header>

<section class="hero">
  <span class="tile" role="img" aria-label="Rider on a horse clearing a jump" style="background:linear-gradient(160deg,#6f8f4e,#3e5a2a)"></span>
  <span class="tile" role="img" aria-label="Netball players on an outdoor court" style="background:linear-gradient(160deg,#9a7a5a,#6b4b35)"></span>
  <span class="tile" role="img" aria-label="Hockey players on a grass field" style="background:linear-gradient(160deg,#8ca46a,#5f7a3c)"></span>
  <span class="tile" role="img" aria-label="Runner crossing a finish line" style="background:linear-gradient(160deg,#b2553e,#6e8a4a)"></span>
  <span class="tile" role="img" aria-label="Student in a blazer at a wardrobe" style="background:linear-gradient(160deg,#c9c2b0,#2f5e2c)"></span>
  <span class="tile" role="img" aria-label="Tree lined school driveway" style="background:linear-gradient(160deg,#4a6d30,#2c4a1e)"></span>
  <span class="tile" role="img" aria-label="Students in green blazers under trees" style="background:linear-gradient(160deg,#5f7f45,#2d5426)"></span>
  <span class="tile" role="img" aria-label="Group of pupils gathered outdoors" style="background:linear-gradient(160deg,#6d5a48,#3d4a2a)"></span>
  <span class="tile" role="img" aria-label="Sports field with hills behind" style="background:linear-gradient(180deg,#b7c6c9,#5f8a3e 55%,#43682a)"></span>
  <span class="tile" role="img" aria-label="Pupils working in a science laboratory" style="background:linear-gradient(160deg,#d7d3cb,#8a8477)"></span>
</section>

<section class="wrap welcome">
  <h2 class="heading">Welcome to <span>Veltrasham College</span></h2>
  <div class="welcome-text">
    <p>Welcome to Veltrasham Group of Schools where our School Motto is 'Tabelana' meaning Togetherness. We aim to work together in every aspect of School life, from academics to sport. Veltrasham College opened on 16th February 1949 and occupies 120 ha of land amidst the low hills of the Tessaly Range, 8km west of Marenvale. This location encourages focus on School life away from the distractions and hustle and bustle of the larger towns.</p>
    <p>The day scholars have the option of selected bus drop off points for parents to collect day scholars closer to home. Veltrasham College offers a wide range of academic subjects alongside a varied sport and extra-curricular program.</p>
  </div>
  <div class="video" role="img" aria-label="Video still of the school building and garden path">
    <svg width="50" height="50" viewBox="0 0 50 50"><circle cx="25" cy="25" r="22" fill="rgba(0,0,0,.35)" stroke="#fff" stroke-width="3"/><path d="M20 15l14 10-14 10z" fill="#fff"/></svg>
  </div>
</section>

<div class="rule" style="top:946px"></div>

<section class="wrap notes">
  <article class="note">
    <h2 class="heading">Headmaster's <span>Welcome Note</span></h2>
    <div class="note-body">
      <span class="note-photo" role="img" aria-label="Portrait of the headmaster" style="background:linear-gradient(160deg,#c7ccd3,#7e8a96)"></span>
      <div class="note-copy">Welcome to Veltrasham College. Here at the College we aim to encourage each pupil to be a self-confident, well rounded individual. We aim to propel them to the highest level of achievement in both academics and extra-curricular activities to provide them with the life skills they will need when they leave the College and to prepare them to be of value to society.
        <br><span class="btn-outline">Read More</span></div>
    </div>
  </article>
  <article class="note">
    <h2 class="heading">Memorial Garden <span>Opened Speech Day 2011</span></h2>
    <div class="note-body">
      <span class="note-photo" role="img" aria-label="Pupils beside the memorial garden plaque" style="background:linear-gradient(160deg,#5a6b3e,#3a3026)"></span>
      <div class="note-copy">Every year the Lower Sixes choose a fundraising project - something for the community like a local orphanage or a local retirement home and then also do something to uplift the school. To uplift the school, the Lower Six Class of 2010 decided that they would like to honour and remember people who played a part in the development of the school.
        <br><span class="btn-outline">Read More</span></div>
    </div>
  </article>
</section>

<section class="wrap calendar">
  <h2 class="heading">School <span>Calender</span></h2>
  <table class="cal">
    <thead><tr><th></th><th>First Term</th><th>Second Term</th><th>Third Term</th></tr></thead>
    <tbody>
      <tr class="shade"><td class="label">Begins</td><td>Tuesday 14th January</td><td>Tuesday 13th May</td><td>Tuesday 9th September</td></tr>
      <tr><td class="label">1st Fixture Free</td><td>Friday 31st January –<br>Monday 3rd February</td><td>Friday 30th May –<br>Monday 2nd June</td><td>Friday 26th September –<br>Monday 29th September</td></tr>
      <tr class="shade"><td class="label">Half-Term</td><td>Thursday 20th February –<br>Tuesday 25th February</td><td>Thursday 26th June –<br>Tuesday 1st July</td><td>Thursday 16th October –<br>Tuesday 21st October</td></tr>
      <tr><td class="label">2nd Fixture Free</td><td>Friday 14th March –<br>Monday 17th March</td><td>Friday 18th July –<br>Monday 21st July</td><td>Friday 7th November –<br>Monday 10th November</td></tr>
      <tr class="shade"><td class="label">Term Ends</td><td>Thursday 10th April</td><td>Friday 7th August</td><td>Thursday 4th December</td></tr>
    </tbody>
  </table>
</section>

<section class="wrap downloads">
  <span class="btn-yellow">Download Registration Form</span>
  <span class="btn-yellow">2nd Term 2014 Termly Calendar</span>
</section>

<section class="wrap events">
  <h2 class="heading">Upcoming <span>Events</span></h2>
  <div class="event-list">
    <div class="event"><span class="event-photo" role="img" aria-label="Basketball players on a court" style="display:block;background:linear-gradient(160deg,#a36a4c,#6b4a36)"></span><div class="event-date">Fri 25 July 2014</div><div class="event-title">Basketball NRSA Top Schools</div></div>
    <div class="event"><span class="event-photo" role="img" aria-label="Pupils performing on a field" style="display:block;background:linear-gradient(160deg,#7b9a58,#4d6b32)"></span><div class="event-date">Sat 02 Aug 2013</div><div class="event-title">School Play - Public Performance</div></div>
    <div class="event"><span class="event-photo" role="img" aria-label="Group of students under trees" style="display:block;background:linear-gradient(160deg,#6d8a4a,#3e4e2a)"></span><div class="event-date">Thurs 07 Aug 2013</div><div class="event-title">Consultation for 4L, 5B, L6, U6</div></div>
  </div>
  <div class="sports">
    <h2 class="heading">Sports <span>Announcements</span></h2>
    <ul><li>- Rugby</li><li>- Hockey Boys</li><li>- Soccer</li><li>- Hockey Girls</li><li>- Basketball Girls</li></ul>
  </div>
</section>

<div class="rule" style="top:2211px"></div>

<section class="wrap partners">
  <div class="partner"><i></i></div>
  <div class="partner"><i></i></div>
  <div class="partner"><i></i></div>
  <div class="partner"><i></i></div>
</section>

<footer class="site-footer">
  <div class="contacts">
    <h2 class="heading footer-title">Get in <span>Touch</span></h2>
    <div class="contact-grid">
      <div class="contact">
        <svg width="30" height="30" viewBox="0 0 30 30"><circle cx="15" cy="15" r="13" fill="none" stroke="#f3e316" stroke-width="2"/><path d="M15 8a4.5 4.5 0 0 0-4.5 4.5c0 3.4 4.5 9 4.5 9s4.5-5.6 4.5-9A4.5 4.5 0 0 0 15 8z" fill="#f3e316"/><circle cx="15" cy="12.5" r="1.6" fill="#0c5a20"/></svg>
        <div><strong>Veltrasham College</strong>Lorem ipsum dolor amet<br>dosis lets us 256894</div>
      </div>
      <div class="contact">
        <svg width="30" height="30" viewBox="0 0 30 30"><circle cx="15" cy="15" r="13" fill="none" stroke="#f3e316" stroke-width="2"/><path d="M8 11l4.5-2 5 2 4.5-2v10l-4.5 2-5-2L8 21z" fill="none" stroke="#f3e316" stroke-width="1.6"/></svg>
        <div><strong>Map</strong>Click here to see directions</div>
      </div>
      <div class="contact">
        <svg width="30" height="30" viewBox="0 0 30 30"><circle cx="15" cy="15" r="13" fill="none" stroke="#f3e316" stroke-width="2"/><path d="M11 8h3l1.5 4-2 1.5a9 9 0 0 0 3.5 3.5l1.5-2 4 1.5v3a2 2 0 0 1-2 2A12 12 0 0 1 9 10a2 2 0 0 1 2-2z" fill="#f3e316"/></svg>
        <div><strong>Phone Number</strong>0772 604 117 / 0772 918 304</div>
      </div>
      <div class="contact">
        <svg width="30" height="30" viewBox="0 0 30 30"><circle cx="15" cy="15" r="13" fill="none" stroke="#f3e316" stroke-width="2"/><rect x="8" y="10" width="14" height="10" fill="none" stroke="#f3e316" stroke-width="1.6"/><path d="M8 10l7 6 7-6" fill="none" stroke="#f3e316" stroke-width="1.6"/></svg>
        <div><strong>Email Us</strong>admin@veltrasham.example</div>
      </div>
    </div>
  </div>
  <div class="newsletter">
    <h2 class="heading footer-title">Signup <span>Newsletter</span></h2>
    <p>If you would like to be added to the list of parents that receive the School Newsletter, please enter your details below.</p>
    <div class="field">Enter Your Name</div>
    <div class="field">Enter Your Email</div>
    <div class="news-btns"><span class="subscribe">Subscribe</span><span class="unsubscribe">Unsubscribe</span></div>
  </div>
</footer>

<div class="bottom-bar">
  <span>2014 Veltrasham College. All Rights Reserved.</span>
  <span class="social"><b></b><i style="background:#3b5b98"></i><i style="background:#35a9dd"></i><i style="background:#d34836"></i></span>
</div>

</body>
</html>
```